Halvorsen Plumbing LLC business card

Would like a modern looking business card with my new logo

Contact Information for Business Card

Dwight Halvorsen 2417 Birchmont Hollow Rd Maplebrook, VT 06512, Halvorsenplumbingllc@mailnest.example, 203-555-0184

```html
<!DOCTYPE html>
<html lang="en">
<head>
<meta charset="utf-8">
<title>Halvorsen Plumbing LLC – Business Card</title>
<link rel="stylesheet" href="https://fonts.googleapis.com/css2?family=Open+Sans:wght@400;600;700;800&display=swap">
<style>
  :root {
    --backdrop: #999999;
    --card-white: #ffffff;
    --card-dark: #202020;
    --brand-blue: #29abe2;
    --ink: #1f1f1f;
  }
  * { box-sizing: border-box; margin: 0; padding: 0; }
  html, body {
    width: 1200px; height: 1059px; overflow: hidden;
    background: var(--backdrop);
    font-family: "Open Sans", sans-serif;
  }
  .card {
    position: absolute;
    width: 690px; height: 392px;
    border-radius: 18px;
    overflow: hidden;
  }
  .card--front { left: 256px; top: 89px; background: var(--card-white); }
  .card--back  { left: 254px; top: 569px; background: var(--card-dark); }

  .wordmark {
    position: absolute;
    display: flex; align-items: center; gap: 12px;
    font-weight: 800;
    text-transform: uppercase;
    line-height: 1;
  }
  .wordmark__square { width: 14px; height: 14px; background: var(--brand-blue); flex: none; }
  .wordmark__name { display: flex; flex-direction: column; gap: 6px; }
  .wordmark__line1 { letter-spacing: 1px; }
  .wordmark__line2 { letter-spacing: 4px; }

  .card--front .wordmark { left: 30px; top: 44px; color: var(--ink); }
  .card--front .wordmark__line1 { font-size: 38px; }
  .card--front .wordmark__line2 { font-size: 15px; }

  .card--back .wordmark { left: 127px; top: 148px; color: #ffffff; }
  .card--back .wordmark__line1 { font-size: 62px; }
  .card--back .wordmark__line2 { font-size: 24px; letter-spacing: 7px; }

  .name-band {
    position: absolute; left: 0; top: 153px;
    width: 520px; height: 59px;
    background: var(--brand-blue);
  }
  .name-band__text {
    position: absolute; left: 30px; top: 9px;
    color: #ffffff; font-size: 34px; font-weight: 600;
    line-height: 40px;
    text-transform: uppercase; letter-spacing: 0.2px;
    white-space: nowrap;
  }
  .tap-art { position: absolute; left: 450px; top: 60px; }

  .address {
    position: absolute; left: 30px; top: 227px;
    font-size: 18px; line-height: 22px; color: var(--ink);
  }
  .contacts { position: absolute; left: 30px; top: 284px; list-style: none; }
  .contacts li {
    display: flex; align-items: center; gap: 7px;
    font-size: 18px; line-height: 26px; color: var(--ink);
    white-space: nowrap;
  }
  .contacts svg { width: 14px; height: 14px; flex: none; fill: var(--brand-blue); }
</style>
</head>
<body>

<section class="card card--front" aria-label="Card front">
  <div class="wordmark">
    <div class="wordmark__name">
      <span class="wordmark__line1">Halvorsen</span>
      <span class="wordmark__line2">Plumbing LLC</span>
    </div>
    <span class="wordmark__square"></span>
  </div>

  <svg class="tap-art" width="200" height="190" viewBox="0 0 200 190" role="img" aria-label="Illustration of a blue water tap extending from the name band">
    <path d="M0 93 H70 V18 Q70 0 88 0 H180 Q200 0 200 20 V188 H150 V152 H0 Z" fill="var(--brand-blue)"/>
  </svg>

  <div class="name-band"><span class="name-band__text">Dwight Halvorsen</span></div>

  <p class="address">2417 Birchmont Hollow Rd<br>Maplebrook, VT 06512</p>

  <ul class="contacts">
    <li>
      <svg viewBox="0 0 24 24" aria-hidden="true"><path d="M6.6 10.8a15.1 15.1 0 0 0 6.6 6.6l2.2-2.2a1 1 0 0 1 1-.25 11.4 11.4 0 0 0 3.6.57 1 1 0 0 1 1 1V20a1 1 0 0 1-1 1A17 17 0 0 1 3 4a1 1 0 0 1 1-1h3.5a1 1 0 0 1 1 1c0 1.25.2 2.45.57 3.57a1 1 0 0 1-.25 1z"/></svg>
      203-555-0184
    </li>
    <li>
      <svg viewBox="0 0 24 24" aria-hidden="true"><path d="M2 5h20v14H2z M3.5 6.5 12 13l8.5-6.5" stroke="#fff" stroke-width="1.5"/></svg>
      Halvorsenplumbingllc@mailnest.example
    </li>
    <li>
      <svg viewBox="0 0 24 24" aria-hidden="true"><circle cx="12" cy="12" r="10"/><path d="M2 12h20M12 2c3 3 3 17 0 20M12 2c-3 3-3 17 0 20" stroke="#fff" stroke-width="1.3" fill="none"/></svg>
      www.Halvorsenplumbingllc.example
    </li>
  </ul>
</section>

<section class="card card--back" aria-label="Card back">
  <div class="wordmark">
    <div class="wordmark__name">
      <span class="wordmark__line1">Halvorsen</span>
      <span class="wordmark__line2">Plumbing LLC</span>
    </div>
    <span class="wordmark__square"></span>
  </div>
</section>

</body>
</html>
```